Larkmoor Capital Partners need a desert themed website!

We need a web design and development for our informational website for our new company named Larkmoor Capital Partners. We would like it to be desert themed and it can be color or black and white. We would like it to be classy and clean, while also talking to the benefits of investment partner with us.

We're thinking probably a home page with a nice image of a Scottsdale landscape, then other pages would What we offer our partners page (or other wording if you find something better), a meet the founder page, and a contact us page.

What we offer our partners (or other wording if you think of something better):
Our investors offer an opportunity to families that cannot usually get approved for a mortgage, to be able to become future homeowners. Thus, Benefiting both the investors and local surrounding community members. Our investors get to both have all the benefits of an investment with receiving above market rates of return to themselves and helping families find homes at the same time.

Maybe also build an infographic with these benefits: Safety, Security, Long-term investment horizon, cashflow, tax benefits, above market rate of return, and capital growth.

And a meet the founder page. With my headshot.

Dale Corwith is a private equity investor providing significantly above market returns to his investment partners while taking the time to be involved with his community and family. Dale first honed his skills in taking calculated risk decisions while very young where he took on playing poker professionally. He succeeded at the highest levels for over a decade competing in high stakes professional cash games around the world.

From the poker world he transitioned to investing in public and private markets. He took an approach of knowing the companies he invests in intimately and after over 10,000 hours of research became known in his community as the person to get investment advice on the electric vehicle industry for his voracious research and expert insight.

He now invests in single family homes in the Phoenix market using his past experience analyzing probabilistic outcomes and comparing the ROIs of different potential strategies. These skills have contributed to his success in investing in companies where he used his ability to assess risk to reward ratios to significantly outperform the market over an extended period.

Contact page we want my email Dale@LarkmoorFunds.example, my instagram: @DaleCorwith, and my linkedin https://www.profilehub.example/in/dale-corwith-58172036/

I have included my headshot for the about me page. I've included some saguaro generated images feel free to incorporate into the website (or make them the company logo), or not, whatever you feel gives the best look for the website.

```html
<!DOCTYPE html>
<html lang="en">
<head>
<meta charset="UTF-8">
<title>Larkmoor Capital Partners</title>
<link href="https://fonts.googleapis.com/css2?family=Poppins:wght@300;400;500;600&display=swap" rel="stylesheet">
<style>
  :root{
    --olive:#46411c;
    --olive-dark:#3a3616;
    --cream:#fdfbea;
    --cream-deep:#f7f1d6;
    --white:#ffffff;
    --ink:#2b2a22;
    --muted:#55534a;
    --accent:#d8bf63;
    --sand:#e9c9a0;
    --sky:#f4e6cf;
  }
  *{box-sizing:border-box;margin:0;padding:0}
  html,body{width:1200px;height:3104px;overflow:hidden}
  body{font-family:'Poppins',sans-serif;color:var(--ink);background:var(--white);position:relative}
  a{color:inherit;text-decoration:none}

  .site-header{position:absolute;top:0;left:0;width:1200px;height:112px;background:var(--white);display:flex;align-items:center;justify-content:space-between;padding:0 72px}
  .brand{font-size:26px;font-weight:500;color:var(--ink)}
  .main-nav{display:flex;gap:34px;font-size:15px;font-weight:500}
  .main-nav a.active{color:var(--accent)}

  .hero{position:absolute;top:112px;left:0;width:1200px;height:656px;background:linear-gradient(90deg,var(--cream-deep) 0%,var(--cream) 45%,#f6ead2 60%)}
  .hero-scene{position:absolute;top:0;right:0;width:660px;height:656px;background:linear-gradient(180deg,#f8efdd 0%,#f1dcc0 45%,#e2b98f 62%,#d9a97b 75%,#b9a06e 100%);-webkit-mask-image:linear-gradient(90deg,transparent 0,#000 140px);mask-image:linear-gradient(90deg,transparent 0,#000 140px)}
  .hero-copy{position:absolute;left:152px;top:146px}
  .hero-kicker{font-size:32px;font-weight:500;margin-bottom:12px}
  .hero-title{font-size:64px;font-weight:400;line-height:1.12;letter-spacing:1px;text-transform:uppercase}
  .hero-sub{font-size:52px;font-weight:400;line-height:1.2;margin-top:4px}
  .btn{display:inline-block;background:var(--olive);color:var(--white);font-size:16px;padding:14px 34px}
  .hero .btn{position:absolute;left:152px;top:444px}
  .slider-dots{position:absolute;left:548px;top:572px;display:flex;gap:8px;align-items:center}
  .slider-dots span{display:block;height:6px;border-radius:3px;background:#cfc7a8}
  .slider-dots span.on{width:28px;background:var(--olive)}
  .slider-dots span.off{width:8px}

  .about{position:absolute;top:768px;left:0;width:1200px;height:692px;background:var(--white)}
  .portrait-ring{position:absolute;left:76px;top:100px;width:488px;height:488px;border:3px solid var(--olive);border-radius:50%}
  .portrait{position:absolute;left:100px;top:124px;width:440px;height:440px;border-radius:50%;background:radial-gradient(circle at 50% 40%,#c9a58e 0%,#a98570 40%,#d8d0c4 75%)}
  .about-copy{position:absolute;left:668px;top:160px;width:440px}
  .section-title{font-size:48px;font-weight:400;color:var(--ink)}
  .rule{display:flex;align-items:center;gap:6px;margin:14px 0 0}
  .rule i{display:block;height:1px;width:60px;background:var(--olive)}
  .rule b{display:block;width:7px;height:7px;border:1px solid var(--olive);transform:rotate(45deg)}
  .about-copy h3{font-size:30px;font-weight:400;margin-top:26px}
  .about-copy p{font-size:13px;line-height:1.7;color:var(--muted);margin-top:28px}
  .about-copy .btn{margin-top:32px;font-size:14px;padding:14px 32px}

  .partners{position:absolute;top:1460px;left:0;width:1200px;height:420px;background:var(--cream);text-align:center}
  .partners .section-title{margin-top:118px}
  .partners .rule{justify-content:center}
  .partners p{width:820px;margin:34px auto 0;font-size:15px;line-height:1.9;color:var(--muted)}

  .benefits{position:absolute;top:1880px;left:0;width:1200px;height:800px;background:var(--white);text-align:center}
  .benefits .section-title{margin-top:140px}
  .benefits .rule{justify-content:center}
  .benefit-grid{position:absolute;left:152px;top:302px;width:960px;display:grid;grid-template-columns:repeat(4,240px);row-gap:54px}
  .benefit{display:flex;flex-direction:column;align-items:center}
  .benefit svg{width:100px;height:100px}
  .benefit span{margin-top:14px;font-size:17px;font-weight:500;line-height:1.3;text-transform:uppercase;width:180px}

  .site-footer{position:absolute;top:2680px;left:0;width:1200px;height:424px;background:var(--cream)}
  .social{position:absolute;top:92px;left:0;width:1200px;display:flex;justify-content:center;gap:22px}
  .social a{width:66px;height:66px;border-radius:50%;background:var(--olive);border:4px solid var(--cream);box-shadow:0 0 0 2px var(--olive)}
  .contact-row{position:absolute;top:214px;left:220px;display:flex;gap:0}
  .contact-item{display:flex;gap:14px;width:256px;font-size:12px;line-height:1.5;color:var(--muted)}
  .contact-item .ico{width:26px;height:26px;background:var(--olive);flex:none;display:flex;align-items:center;justify-content:center}
  .footer-line{position:absolute;top:290px;left:220px;width:820px;height:1px;background:#d6cfad}
  .footer-nav{position:absolute;top:312px;left:0;width:1200px;display:flex;justify-content:center;gap:42px;font-size:14px}
  .copyright{position:absolute;bottom:0;left:0;width:1200px;height:52px;background:var(--olive-dark);color:var(--white);font-size:12px;display:flex;align-items:center;justify-content:center}
</style>
</head>
<body>

<header class="site-header">
  <a class="brand" href="#">Larkmoor Capital Partners</a>
  <nav class="main-nav">
    <a class="active" href="#">HOME</a>
    <a href="#">ABOUT US</a>
    <a href="#">OUR PARTNERS</a>
    <a href="#">CONTACT US</a>
  </nav>
</header>

<section class="hero">
  <div class="hero-scene" role="img" aria-label="Desert landscape with tall saguaro cactus, red rock mesas and desert plants under a warm sky"></div>
  <div class="hero-copy">
    <p class="hero-kicker">Welcome To</p>
    <h1 class="hero-title">Larkmoor<br>Capital</h1>
    <p class="hero-sub">Partners</p>
  </div>
  <a class="btn" href="#">Know More</a>
  <div class="slider-dots"><span class="on"></span><span class="off"></span></div>
</section>

<section class="about">
  <div class="portrait-ring"></div>
  <div class="portrait" role="img" aria-label="Headshot of founder Dale Corwith"></div>
  <div class="about-copy">
    <h2 class="section-title">About Us</h2>
    <div class="rule"><i></i><b></b><i></i></div>
    <h3>Meet the Founder</h3>
    <p>Dale Corwith is a private equity investor providing significantly above market returns to his investment partners while taking the time to be involved with his community and family. Dale first honed his skills in taking calculated risk decisions while very young where he took on playing poker professionally.</p>
    <a class="btn" href="#">READ MORE</a>
  </div>
</section>

<section class="partners">
  <h2 class="section-title">Our Partners</h2>
  <div class="rule"><i></i><b></b><i></i></div>
  <p>Our investors offer an opportunity to families that cannot usually get approved for a mortgage, to be able to become future homeowners. Thus, Benefiting both the investors and local surrounding community members. Our investors get to both have all the benefits of an investment with receiving above market rates of return to themselves and helping families find homes at the same time.</p>
</section>

<section class="benefits">
  <h2 class="section-title">Our Benefits</h2>
  <div class="rule"><i></i><b></b><i></i></div>
  <div class="benefit-grid">
    <div class="benefit">
      <svg viewBox="0 0 100 100"><circle cx="50" cy="50" r="48" fill="none" stroke="#46411c" stroke-width="2"/><circle cx="50" cy="50" r="42" fill="#46411c"/><path d="M50 28 L66 34 V50 C66 62 58 70 50 73 C42 70 34 62 34 50 V34 Z" fill="none" stroke="#fff" stroke-width="2.5"/><path d="M43 50 L48 55 L58 44" fill="none" stroke="#fff" stroke-width="2.5"/></svg>
      <span>Safety</span>
    </div>
    <div class="benefit">
      <svg viewBox="0 0 100 100"><circle cx="50" cy="50" r="48" fill="none" stroke="#46411c" stroke-width="2"/><circle cx="50" cy="50" r="42" fill="#46411c"/><path d="M50 28 L66 34 V50 C66 62 58 70 50 73 C42 70 34 62 34 50 V34 Z" fill="none" stroke="#fff" stroke-width="2.5"/><rect x="43" y="47" width="14" height="11" fill="none" stroke="#fff" stroke-width="2.2"/><path d="M45 47 V43 A5 5 0 0 1 55 43 V47" fill="none" stroke="#fff" stroke-width="2.2"/></svg>
      <span>Security</span>
    </div>
    <div class="benefit">
      <svg viewBox="0 0 100 100"><circle cx="50" cy="50" r="48" fill="none" stroke="#46411c" stroke-width="2"/><circle cx="50" cy="50" r="42" fill="#46411c"/><circle cx="50" cy="42" r="12" fill="none" stroke="#fff" stroke-width="2.5"/><path d="M50 35 V49 M46 39 H53 M47 45 H54" stroke="#fff" stroke-width="2"/><path d="M30 66 L40 60 H52 L60 64 L70 58" fill="none" stroke="#fff" stroke-width="2.5"/></svg>
      <span>Long-Term Investment Horizon</span>
    </div>
    <div class="benefit">
      <svg viewBox="0 0 100 100"><circle cx="50" cy="50" r="48" fill="none" stroke="#46411c" stroke-width="2"/><circle cx="50" cy="50" r="42" fill="#46411c"/><circle cx="50" cy="50" r="18" fill="none" stroke="#fff" stroke-width="2.5"/><path d="M50 39 V61 M45 44 H54 M46 50 H55 M45 56 H54" stroke="#fff" stroke-width="2"/><path d="M28 36 A25 25 0 0 1 40 28" fill="none" stroke="#fff" stroke-width="2.5"/><path d="M72 64 A25 25 0 0 1 60 72" fill="none" stroke="#fff" stroke-width="2.5"/></svg>
      <span>Cashflow</span>
    </div>
    <div class="benefit">
      <svg viewBox="0 0 100 100"><circle cx="50" cy="50" r="48" fill="none" stroke="#46411c" stroke-width="2"/><circle cx="50" cy="50" r="42" fill="#46411c"/><rect x="34" y="30" width="28" height="38" fill="none" stroke="#fff" stroke-width="2.5"/><path d="M39 40 H57 M39 47 H57 M39 54 H50" stroke="#fff" stroke-width="2"/><circle cx="62" cy="62" r="8" fill="#46411c" stroke="#fff" stroke-width="2.5"/></svg>
      <span>Tax Benefits</span>
    </div>
    <div class="benefit">
      <svg viewBox="0 0 100 100"><circle cx="50" cy="50" r="48" fill="none" stroke="#46411c" stroke-width="2"/><circle cx="50" cy="50" r="42" fill="#46411c"/><path d="M30 68 H70" stroke="#fff" stroke-width="2.5"/><rect x="34" y="54" width="7" height="14" fill="#fff"/><rect x="46" y="46" width="7" height="22" fill="#fff"/><rect x="58" y="38" width="7" height="30" fill="#fff"/><path d="M32 46 L46 34 L54 40 L68 28 M62 28 H68 V34" fill="none" stroke="#fff" stroke-width="2.2"/></svg>
      <span>Above Market Rate of Return</span>
    </div>
    <div class="benefit">
      <svg viewBox="0 0 100 100"><circle cx="50" cy="50" r="48" fill="none" stroke="#46411c" stroke-width="2"/><circle cx="50" cy="50" r="42" fill="#46411c"/><path d="M30 68 H70" stroke="#fff" stroke-width="2.5"/><rect x="36" y="56" width="7" height="12" fill="none" stroke="#fff" stroke-width="2"/><rect x="47" y="48" width="7" height="20" fill="none" stroke="#fff" stroke-width="2"/><rect x="58" y="40" width="7" height="28" fill="none" stroke="#fff" stroke-width="2"/><path d="M34 44 L60 28 M54 27 H61 V34" fill="none" stroke="#fff" stroke-width="2.2"/></svg>
      <span>Capital Growth</span>
    </div>
  </div>
</section>

<footer class="site-footer">
  <div class="social">
    <a href="#" aria-label="Instagram @DaleCorwith"></a>
    <a href="https://www.profilehub.example/in/dale-corwith-58172036/" aria-label="Professional profile"></a>
  </div>
  <div class="contact-row">
    <div class="contact-item">
      <span class="ico"><svg width="14" height="14" viewBox="0 0 24 24"><path d="M6 3 L10 3 L11 8 L8 10 C9.5 13 11 14.5 14 16 L16 13 L21 14 L21 18 C21 19.5 19.5 21 18 21 C10 20.5 3.5 14 3 6 C3 4.5 4.5 3 6 3 Z" fill="#fff"/></svg></span>
      <div>Call Us<br>(480) 555-0142</div>
    </div>
    <div class="contact-item">
      <span class="ico"><svg width="14" height="14" viewBox="0 0 24 24"><rect x="3" y="6" width="18" height="12" fill="none" stroke="#fff" stroke-width="2"/><path d="M3 6 L12 13 L21 6" fill="none" stroke="#fff" stroke-width="2"/></svg></span>
      <div>Email Us<br>Dale@LarkmoorFunds.example</div>
    </div>
    <div class="contact-item">
      <span class="ico"><svg width="14" height="14" viewBox="0 0 24 24"><path d="M12 2 C8 2 5 5 5 9 C5 14 12 22 12 22 C12 22 19 14 19 9 C19 5 16 2 12 2 Z" fill="#fff"/><circle cx="12" cy="9" r="2.5" fill="#46411c"/></svg></span>
      <div>Address Goes Here<br>City Line Here</div>
    </div>
  </div>
  <div class="footer-line"></div>
  <nav class="footer-nav">
    <a href="#">HOME</a>
    <a href="#">ABOUT US</a>
    <a href="#">OUR PARTNERS</a>
    <a href="#">CONTACT US</a>
  </nav>
  <div class="copyright">Copyright © 2024 All Rights Reserved By Company Name</div>
</footer>

</body>
</html>
```